KWT BUSINESS CARD

I'd like a new business card for the folks in my office. I recently became aware of a company that produces extra thick cards that seem to me to make excellent use of embossing. I have a logo that I like so I just need a design that uses embossing effectively, is simple and uses minimal color.

I am uploading our current logo of a tooth with a brush above it. I am also uploading another file with the words of our business. In your design please use the square version of the tooth vs. the strectched version. The original logo is the more square image but please use the words and the fonts of "Wexmoor Dental Group" and incorporate that in the design.

Industry/Entity Type

Business

Colors
ffffff

Requirements
Must have
• Logo, company name (also a part of our existing logo), employee name and title, phone number and website address. Must be simple
Nice to have
• Embossed - Maybe a solid color on the back
Should not have
• Must not be too complex or busy

```html
<!DOCTYPE html>
<html lang="en">
<head>
<meta charset="utf-8">
<title>Wexmoor Dental Group – Business Card</title>
<link href="https://fonts.googleapis.com/css2?family=Varela+Round&display=swap" rel="stylesheet">
<style>
  :root {
    --backdrop: #2b2b2c;
    --card: #e6e8e9;
    --emboss-ink: #d6d9db;
    --emboss-light: rgba(255,255,255,0.9);
    --emboss-dark: rgba(0,0,0,0.22);
    --brand-purple: #8f8bd0;
    --brand-ink: #9a9fa3;
  }
  * { margin: 0; padding: 0; box-sizing: border-box; }
  html, body { width: 1200px; height: 800px; overflow: hidden; }
  body {
    background: var(--backdrop);
    font-family: "Varela Round", "Nunito", sans-serif;
    display: flex;
    align-items: center;
    justify-content: center;
    gap: 44px;
  }
  .card {
    width: 522px;
    height: 298px;
    background: var(--card);
    border-radius: 3px;
    position: relative;
    box-shadow: 0 10px 30px rgba(0,0,0,0.35);
  }
  .embossed {
    color: var(--emboss-ink);
    text-shadow: -1px -1px 0 var(--emboss-light), 1px 1px 1px var(--emboss-dark);
  }

  /* Front: contact side */
  .card-front .contact {
    position: absolute;
    left: 0; right: 0; top: 56px;
    text-align: center;
  }
  .employee-name { font-size: 34px; letter-spacing: 1px; }
  .employee-title { font-size: 19px; letter-spacing: 1.5px; margin-top: 8px; }
  .phone { font-size: 19px; letter-spacing: 1.5px; margin-top: 52px; }
  .website { font-size: 19px; letter-spacing: 1.5px; margin-top: 18px; }

  /* Back: brand side */
  .card-back .brand {
    position: absolute;
    inset: 0;
    display: flex;
    align-items: center;
    justify-content: center;
    gap: 22px;
  }
  .brand-square {
    width: 96px;
    height: 96px;
    background: var(--brand-purple);
  }
  .brand-name {
    color: var(--brand-ink);
    font-size: 30px;
    line-height: 1.15;
    letter-spacing: 1px;
  }
</style>
</head>
<body>
  <section class="card card-back" aria-label="Card back">
    <div class="brand">
      <div class="brand-square"></div>
      <div class="brand-name">Wexmoor<br>Dental Group</div>
    </div>
  </section>

  <section class="card card-front" aria-label="Card front">
    <div class="contact">
      <p class="employee-name embossed">Dana Holloway</p>
      <p class="employee-title embossed">office manager</p>
      <p class="phone embossed">555-014-2280</p>
      <p class="website embossed">www.wexmoordentalgroup.com</p>
    </div>
  </section>
</body>
</html>
```